Postcard Design -- Harbor Bridgeworks

Harbor Bridgeworks believes that when low-income immigrants acquire the right tools (skills and abilities), they can overcome poverty and build a pathway to success as new Americans. We accomplish this through our wraparound strategy, which offers a full range of services designed to help people overcome barriers to the acquisition of the skills and abilities they need to thrive. This process involves recognizing the diverse skills immigrants already possess, resolving immediate needs or problems, identifying opportunities for growth, and monitoring progress toward goals. As a result, clients are able to acquire the skills and abilities they need to thrive as new Americans.

We need a postcard design that follows the Harbor Bridgeworks brand, but also has a heartwarming/holiday feel to it with a cool factor. This postcard will be mailed as an insert with our appeal letter. The purpose of this postcard is to encourage donors who receive it to reuse/mail it to someone else and encourage them to donate to Harbor Bridgeworks.

Target Market(s)

Donors

Industry/Entity Type

Non-Profit

Font styles to use
Sans Serif

Requirements
Must have
• Our Colors: #3276b5 #9bcb3c #fece3e #f04a50
• Double sided Postcard:
• Front side:
• - A design that is welcoming and has a heartwarming/holiday feel to it
• - Our logo
• - and a message (examples: 'Thinking About You'.. 'Giving back to the community'.. 'Celebrate with us'.. 'Sharing the holiday spirit'.. 'Share the cheer'.. 'Invest in our community'..) I'm open to new ideas.
• Back side:
• - Mission Statement
• - We help low-income, Spanish-speaking immigrants acquire the tools they need to thrive.
• - Logo
• - site link (harborbridgeworks.org)
• - donation link (donate.harborbridgeworks.org)
• - Call to action (Invest in Harbor Bridgeworks Today!.. Wishing you Happy Holidays, join me in supporting New-Americans today.. etc)
• - Leave area available for sender info and person receiving info (like a regular postcard)
• - 5087310925
• -FB and Twitter icon
Nice to have
• Postcard Final Dimension: 3.5"x5" (with bleed, PLEASE)
• PROJECT SPECIFICS
• Audience = Donors
• Message = Asking other to invest on Harbor Bridgeworks
• Product = Postcard Design 3.5"x5"
• Font = Sans Serif

```html
<!DOCTYPE html>
<html lang="en">
<head>
<meta charset="utf-8">
<title>Harbor Bridgeworks Holiday Postcard</title>
<link rel="stylesheet" href="https://fonts.googleapis.com/css2?family=Lato:ital,wght@0,400;0,700;1,400;1,700&family=Oswald:wght@300;700&family=Roboto+Condensed:wght@700&display=swap">
<style>
  :root {
    --brand-blue: #0f75b6;
    --brand-green: #7fb13c;
    --brand-yellow: #fdbf13;
    --brand-red: #b7202e;
    --band-red: #d11d27;
    --ink: #1f1f1f;
    --muted: #2c2c2c;
    --paper: #ffffff;
    --stage: #e9e9e9;
    --rule: #8a8a8a;
  }
  * { box-sizing: border-box; margin: 0; padding: 0; }
  html, body { width: 902px; height: 1200px; overflow: hidden; background: var(--stage); }
  body { position: relative; font-family: "Lato", Arial, sans-serif; }

  .card { position: absolute; left: 46px; width: 810px; height: 560px; background: var(--paper); overflow: hidden; box-shadow: 0 2px 10px rgba(0,0,0,.25); }
  .card--front { top: 40px; }
  .card--back { top: 620px; }
  .card svg.shapes { position: absolute; inset: 0; }

  /* front */
  .headline { position: absolute; right: 38px; top: 24px; text-align: right; color: var(--brand-red); font-family: "Oswald", Arial, sans-serif; line-height: 1.05; }
  .headline__lead { font-weight: 300; font-size: 50px; letter-spacing: .5px; display: block; }
  .headline__main { font-weight: 700; font-size: 52px; display: block; }
  .tagline { position: absolute; right: 0; top: 142px; width: 340px; height: 64px; padding: 6px 40px 0 0; background: linear-gradient(90deg, rgba(127,177,60,0) 0%, var(--brand-green) 22%); color: #fff; font-style: italic; font-weight: 700; font-size: 18px; line-height: 1.3; text-align: right; }
  .brand-name { position: absolute; color: var(--brand-blue); font-weight: 700; font-family: "Lato", Arial, sans-serif; }
  .card--front .brand-name { right: 56px; top: 318px; font-size: 24px; }
  .brand-dot { display: inline-block; width: 14px; height: 14px; background: var(--brand-blue); border-radius: 50%; margin-right: 8px; vertical-align: middle; }

  .contact { position: absolute; list-style: none; color: #fff; font-style: italic; font-size: 18px; }
  .contact li { display: flex; align-items: center; height: 33px; }
  .contact svg { width: 14px; height: 16px; margin-right: 14px; flex: none; }
  .card--front .contact { left: 30px; top: 440px; }

  .follow { position: absolute; right: 16px; bottom: 38px; display: flex; align-items: center; font-size: 14px; color: var(--muted); }
  .follow span { margin-right: 10px; }
  .follow i { display: inline-block; width: 20px; height: 20px; margin-left: 9px; border-radius: 3px; }

  /* back */
  .mission { position: absolute; left: 22px; top: 18px; width: 360px; font-family: "Roboto Condensed", Arial, sans-serif; font-size: 20px; line-height: 1.3; color: var(--brand-blue); }
  .mission__end { color: #2f7a1d; }
  .card--back .brand-name { left: 40px; top: 195px; font-size: 23px; }
  .links { position: absolute; left: 26px; top: 240px; font-style: italic; font-size: 18px; color: var(--ink); line-height: 1.35; }
  .links b { color: #3a7d1c; font-weight: 700; }
  .cta-band { position: absolute; left: 0; top: 298px; width: 380px; height: 44px; background: var(--brand-blue); color: #fff; font-family: "Oswald", Arial, sans-serif; font-weight: 300; font-size: 24px; line-height: 44px; padding-left: 18px; white-space: nowrap; }
  .cta-note { position: absolute; left: 22px; top: 350px; width: 290px; font-size: 17px; line-height: 1.3; color: var(--ink); }
  .card--back .contact { left: 22px; top: 442px; font-size: 16px; font-weight: 700; }
  .card--back .contact li { height: 32px; }
  .contact .wrap { line-height: 1.2; }

  .photo-ring { position: absolute; border-radius: 50%; border: 4px solid #fff; box-shadow: 0 2px 6px rgba(0,0,0,.35); }
  .photo-ring--snow { left: 308px; top: 70px; width: 186px; height: 186px; background: radial-gradient(circle at 45% 55%, #f3f4f6 0%, #b9c2cc 45%, #4b5868 100%); }
  .photo-ring--family { left: 362px; top: 230px; width: 162px; height: 162px; background: radial-gradient(circle at 50% 55%, #e9a58a 0%, #c98b6f 40%, #6f8a56 100%); }
  .photo-ring--kids { left: 300px; top: 380px; width: 150px; height: 150px; background: radial-gradient(circle at 50% 55%, #e6b08e 0%, #c74b3c 40%, #4a8fd1 100%); }

  .stamp { position: absolute; left: 710px; top: 18px; width: 77px; height: 94px; border: 1px solid var(--rule); }
  .address-line { position: absolute; left: 560px; width: 230px; border-top: 1px solid var(--rule); }
</style>
</head>
<body>

<section class="card card--front" aria-label="Postcard front">
  <svg class="shapes" viewBox="0 0 810 560" width="810" height="560" aria-hidden="false">
    <defs>
      <linearGradient id="heroTone" x1="0" y1="0" x2="1" y2="1">
        <stop offset="0" stop-color="#7aa24a"/>
        <stop offset=".35" stop-color="#d9a98a"/>
        <stop offset=".7" stop-color="#c9477a"/>
        <stop offset="1" stop-color="#e7d7c6"/>
      </linearGradient>
      <linearGradient id="heroFade" x1="0" y1="0" x2="1" y2="0">
        <stop offset=".55" stop-color="#fff" stop-opacity="0"/>
        <stop offset="1" stop-color="#fff" stop-opacity="1"/>
      </linearGradient>
    </defs>
    <g role="img" aria-label="Photo of a smiling mother with two young daughters outdoors, holding a seedling">
      <rect x="0" y="0" width="500" height="440" fill="url(#heroTone)"/>
      <rect x="0" y="0" width="500" height="440" fill="url(#heroFade)"/>
    </g>
    <path d="M150 405 C 330 378, 470 420, 560 455 C 660 490, 740 420, 810 300 L810 560 L0 560 Z" fill="var(--brand-blue)"/>
    <path d="M190 430 C 360 402, 480 440, 570 478 C 670 515, 750 440, 810 345 L810 560 L0 560 Z" fill="var(--brand-yellow)"/>
    <path d="M0 422 C 190 400, 380 420, 520 480 C 620 525, 720 548, 810 550 L810 560 L0 560 Z" fill="var(--brand-red)"/>
  </svg>

  <h1 class="headline"><span class="headline__lead">GIVING BACK TO THE</span><span class="headline__main">COMMUNITY</span></h1>
  <p class="tagline">Every new American deserves<br>the opportunity to thrive!</p>
  <div class="brand-name"><span class="brand-dot"></span>Harbor Bridgeworks</div>

  <ul class="contact">
    <li><svg viewBox="0 0 14 16"><rect x="2" y="0" width="10" height="16" rx="2" fill="var(--brand-yellow)"/><rect x="4" y="2" width="6" height="7" fill="var(--brand-red)"/></svg>(508) 731-0925</li>
    <li><svg viewBox="0 0 16 16"><circle cx="8" cy="8" r="7" fill="var(--brand-yellow)"/><path d="M1 8h14M8 1v14" stroke="var(--brand-red)" stroke-width="1"/></svg>www.harborbridgeworks.org</li>
    <li><svg viewBox="0 0 14 16"><path d="M7 0C3 0 1 3 1 6c0 4 6 10 6 10s6-6 6-10c0-3-2-6-6-6z" fill="var(--brand-yellow)"/><circle cx="7" cy="6" r="2" fill="var(--brand-red)"/></svg>58 Seabright Avenue, Fairhaven, MA 02719</li>
  </ul>

  <div class="follow"><span>Follow Us on</span><i style="background:#3b5998"></i><i style="background:#38a1f3"></i><i style="background:#0e76a8"></i><i style="background:#dc4a38"></i></div>
</section>

<section class="card card--back" aria-label="Postcard back">
  <svg class="shapes" viewBox="0 0 810 560" width="810" height="560">
    <path d="M0 0 L400 0 C 500 90, 520 260, 500 360 C 485 440, 470 500, 460 560 L0 560 Z" fill="var(--brand-green)"/>
    <path d="M0 0 L370 0 C 455 90, 470 250, 455 350 C 440 430, 425 500, 415 560 L0 560 Z" fill="var(--brand-blue)"/>
    <path d="M0 0 L340 0 C 420 90, 430 250, 415 350 C 400 430, 385 500, 375 560 L0 560 Z" fill="var(--brand-yellow)"/>
    <path d="M0 432 L410 432 C 400 480, 385 520, 378 560 L0 560 Z" fill="var(--band-red)"/>
  </svg>

  <p class="mission">We help low-income,<br>Spanish-speaking immigrants acquire<br><span class="mission__end">the tools they need to thrive...</span></p>
  <div class="brand-name"><span class="brand-dot"></span>Harbor Bridgeworks</div>
  <p class="links">Site link: <b>harborbridgeworks.org</b><br>Donation link: <b>donate.harborbridgeworks.org</b></p>
  <div class="cta-band">Invest in Harbor Bridgeworks Today!..</div>
  <p class="cta-note">Wishing you Happy Holidays, join me in supporting New-Americans today...</p>

  <ul class="contact">
    <li><svg viewBox="0 0 14 16"><rect x="2" y="0" width="10" height="16" rx="2" fill="var(--brand-yellow)"/><rect x="4" y="2" width="6" height="7" fill="var(--band-red)"/></svg>(508) 731-0925</li>
    <li><svg viewBox="0 0 16 16"><circle cx="8" cy="8" r="7" fill="var(--brand-yellow)"/><path d="M1 8h14M8 1v14" stroke="var(--band-red)" stroke-width="1"/></svg>www.harborbridgeworks.org</li>
    <li style="height:48px"><svg viewBox="0 0 14 16"><path d="M7 0C3 0 1 3 1 6c0 4 6 10 6 10s6-6 6-10c0-3-2-6-6-6z" fill="var(--brand-yellow)"/><circle cx="7" cy="6" r="2" fill="var(--band-red)"/></svg><span class="wrap">58 Seabright Avenue,<br>Fairhaven, MA 02719</span></li>
  </ul>

  <div class="photo-ring photo-ring--snow" role="img" aria-label="Photo of a couple posing beside a snowman in a winter forest"></div>
  <div class="photo-ring photo-ring--family" role="img" aria-label="Photo of a smiling family of four sitting outdoors"></div>
  <div class="photo-ring photo-ring--kids" role="img" aria-label="Photo of a group of smiling children under a blue sky"></div>

  <div class="stamp" aria-label="Stamp area"></div>
  <div class="address-line" style="top:280px"></div>
  <div class="address-line" style="top:327px"></div>
  <div class="address-line" style="top:375px"></div>
</section>

</body>
</html>
```